Lorna Tess Tresses Fancy Business Card’s

I want my business cards to be elite, original and very classy. I want the business cards to match the colors of my logo and to match the design posted. I would love the design of the picture I posted

I want the card all white .
The dripping on the top of the card I want it to match the pink color in my logo that’s also posted .
I need my logo on the business card !
I need my Instagram- @lorna.tess.tresses__
And my phone number - 582 907 3365

Target Market(s)

My target market is young woman age 23 to older woman to the age of 65
I want both older and younger women to love my design . I don’t want any cheap looking business cards

Industry/Entity Type

Hair And Beauty

Contact Information for Business Card

Add my logo
Add my Instagram- @lorna.tess.tresses__
My number - 582 907 3365
My website- www.lornatesstresses.example

Font styles to use
Serif
Script

Colors
ffffff
e667a6
e34298

Requirements
Must have
• The business cards must have my logo, my number , my website, and my Instagram!
Nice to have
• Nice to have glitter words that match my logo
• The business cards must look classy and mature
• I want them to be very unique!!
Should not have
• Should not have any colors that doesn’t match my logo ! This is very important! Please

```html
<!DOCTYPE html>
<html lang="en">
<head>
<meta charset="utf-8">
<title>Lorna Tess Tresses — Business Card</title>
<link rel="stylesheet" href="https://fonts.googleapis.com/css2?family=Montserrat:wght@400;500;700&display=swap">
<style>
  :root {
    --white: #ffffff;
    --pink: #e34298;
    --pink-soft: #e667a6;
    --backdrop: #f2f2f2;
  }
  * { margin: 0; padding: 0; box-sizing: border-box; }
  html, body {
    width: 1200px;
    height: 1200px;
    overflow: hidden;
    background: var(--backdrop);
    font-family: "Montserrat", sans-serif;
  }
  .card {
    position: absolute;
    left: 252px;
    width: 697px;
    height: 397px;
    background: var(--white);
    overflow: hidden;
  }
  .card--front { top: 109px; }
  .card--back  { top: 652px; }

  .hair-band {
    position: absolute;
    left: 0;
    top: 0;
    width: 697px;
    height: 170px;
  }
  .hair-side {
    position: absolute;
    left: 0;
    top: 0;
    width: 210px;
    height: 397px;
  }

  .brand-name {
    position: absolute;
    left: 0;
    right: 0;
    top: 150px;
    text-align: center;
    color: var(--pink);
    font-weight: 500;
    font-size: 46px;
    line-height: 1.1;
    letter-spacing: 3px;
  }
  .brand-name span {
    display: block;
    font-size: 30px;
    letter-spacing: 14px;
    margin-top: 6px;
  }
  .website {
    position: absolute;
    left: 0;
    right: 0;
    top: 355px;
    text-align: center;
    color: var(--pink);
    font-weight: 500;
    font-size: 16px;
    letter-spacing: 3px;
  }

  .divider {
    position: absolute;
    left: 256px;
    top: 96px;
    width: 2px;
    height: 205px;
    background: var(--pink-soft);
  }
  .contact-icon {
    position: absolute;
    left: 202px;
    width: 22px;
    height: 22px;
  }
  .contact-icon--phone { top: 160px; }
  .contact-icon--social { top: 209px; }
  .contact-text {
    position: absolute;
    left: 294px;
    color: var(--pink-soft);
    font-weight: 700;
    font-size: 22px;
    letter-spacing: 4px;
    white-space: nowrap;
  }
  .contact-text--phone { top: 157px; }
  .contact-text--social { top: 205px; font-size: 20px; letter-spacing: 3px; }
</style>
</head>
<body>

<section class="card card--front">
  <svg class="hair-band" viewBox="0 0 697 170" role="img" aria-label="Flowing pink hair illustration along the top edge">
    <defs>
      <linearGradient id="hairTop" x1="0" y1="0" x2="0" y2="1">
        <stop offset="0" stop-color="#e34298"/>
        <stop offset="1" stop-color="#e667a6"/>
      </linearGradient>
    </defs>
    <path fill="url(#hairTop)" d="M0 0 H697 V168 C660 160 640 140 610 100 C560 80 520 80 480 60 C430 40 400 30 350 10 C300 30 270 40 220 60 C180 80 140 80 90 100 C60 140 40 160 0 168 Z"/>
  </svg>

  <h1 class="brand-name">Lorna Tess<span>TRESSES</span></h1>
  <p class="website">www.lornatesstresses.example</p>
</section>

<section class="card card--back">
  <svg class="hair-side" viewBox="0 0 210 397" role="img" aria-label="Flowing pink hair illustration along the left edge">
    <defs>
      <linearGradient id="hairSide" x1="0" y1="0" x2="1" y2="0">
        <stop offset="0" stop-color="#e34298"/>
        <stop offset="1" stop-color="#e667a6"/>
      </linearGradient>
    </defs>
    <path fill="url(#hairSide)" d="M0 0 H40 C50 30 80 50 78 90 C74 130 70 150 88 180 C100 210 100 240 120 260 C150 290 170 330 200 397 H0 Z"/>
  </svg>

  <svg class="contact-icon contact-icon--phone" viewBox="0 0 24 24" aria-hidden="true">
    <path fill="var(--pink-soft)" d="M6.6 10.8c1.4 2.8 3.8 5.1 6.6 6.6l2.2-2.2c.3-.3.7-.4 1-.2 1.1.4 2.3.6 3.6.6.6 0 1 .4 1 1V20c0 .6-.4 1-1 1C10.6 21 3 13.4 3 4c0-.6.4-1 1-1h3.5c.6 0 1 .4 1 1 0 1.3.2 2.5.6 3.6.1.3 0 .7-.2 1z"/>
  </svg>
  <svg class="contact-icon contact-icon--social" viewBox="0 0 24 24" aria-hidden="true">
    <rect x="3" y="3" width="18" height="18" rx="2" fill="none" stroke="var(--pink-soft)" stroke-width="2.2"/>
  </svg>

  <div class="divider"></div>

  <p class="contact-text contact-text--phone">582 907 3365</p>
  <p class="contact-text contact-text--social">@ lorna.tess.tresses__</p>
</section>

</body>
</html>
```